I need a business card that is professional /minimalistic ( clean edges) to help develop my new business venture that is car valeting / detailing.

I would like to use a black background, white font,red car silhouette above the text.

have now added phone numbers thanks

Industry/Entity Type

Business

Contact Information for Business Card

Gleamcraft Studio,
Valeting & Detailing Specialist,
tel 01638 219054 mob 07814 605193, Dean Marlowe, 7 Hawthorn Rise. East Brackley, Beccles. IP19 3JD

```html
<!DOCTYPE html>
<html lang="en">
<head>
<meta charset="utf-8">
<title>Gleamcraft Studio – Business Card</title>
<link rel="stylesheet" href="https://fonts.googleapis.com/css2?family=Jost:wght@300&display=swap">
<style>
  :root {
    --ink: #f2f2f2;
    --accent: #9a1a1f;
    --accent-deep: #4a0a0d;
    --bg-core: #232323;
    --bg-mid: #111111;
    --bg-edge: #000000;
    --fold-shadow: rgba(0, 0, 0, 0.55);
    --fold-light: rgba(255, 255, 255, 0.035);
  }
  * { margin: 0; padding: 0; box-sizing: border-box; }
  html, body {
    width: 1200px;
    height: 753px;
    overflow: hidden;
    background: var(--bg-edge);
  }
  .card {
    position: relative;
    width: 1200px;
    height: 753px;
    overflow: hidden;
    font-family: "Jost", "Futura", sans-serif;
    font-weight: 300;
    color: var(--ink);
    background:
      radial-gradient(ellipse 620px 520px at 360px 330px, var(--bg-core) 0%, var(--bg-mid) 55%, transparent 100%),
      radial-gradient(ellipse 420px 440px at 970px 330px, #1c1c1c 0%, var(--bg-mid) 55%, transparent 100%),
      var(--bg-edge);
  }
  .fold {
    position: absolute;
    top: 0;
    left: 722px;
    width: 60px;
    height: 100%;
    background: linear-gradient(to right, var(--fold-light) 0, var(--fold-shadow) 2px, transparent 60px);
  }
  .details {
    position: absolute;
    left: 76px;
    top: 291px;
    font-size: 29px;
    line-height: 37.6px;
    letter-spacing: 0.08em;
    text-transform: uppercase;
    list-style: none;
    white-space: nowrap;
  }
  .emblem {
    position: absolute;
    left: 774px;
    top: 312px;
    width: 383px;
    height: 46px;
    border-radius: 4px;
    background: radial-gradient(ellipse 60% 70% at 50% 60%, var(--accent) 0%, var(--accent-deep) 55%, transparent 100%);
    opacity: 0.75;
  }
  .brand {
    position: absolute;
    left: 836px;
    top: 364px;
    font-size: 27px;
    letter-spacing: 0.05em;
    text-transform: uppercase;
    white-space: nowrap;
  }
</style>
</head>
<body>
  <main class="card">
    <div class="fold" aria-hidden="true"></div>
    <ul class="details">
      <li>Valeting &amp; Detailing Specialist,</li>
      <li>Tel 01638 219054 Mob 07814 605193,</li>
      <li>Dean Marlowe, 7 Hawthorn Rise.</li>
      <li>East Brackley, Beccles. IP19 3JD</li>
    </ul>
    <div class="emblem" role="img" aria-label="Area for the red car silhouette logo"></div>
    <p class="brand">Gleamcraft Studio</p>
  </main>
</body>
</html>
```